KPR

we need new ideas for direct mail designs for a furniture retailer SALE

Target Market(s)

Women 25-53

Font styles to use
Sans Serif

Colors

Designer to choose colors to be used in the design.

Requirements
Must have
• Photos of furniture and title design
Nice to have
• refined typography sophisticated color scheme black and white is also good with accent color

```html
<!DOCTYPE html>
<html lang="en">
<head>
<meta charset="utf-8">
<title>Furniture Sale Mailer</title>
<link href="https://fonts.googleapis.com/css2?family=Montserrat:wght@500;700;800&display=swap" rel="stylesheet">
<style>
  :root {
    --paper: #f7f7f7;
    --ink: #111111;
    --accent: #5de0b5;
    --white: #ffffff;
    --photo-office: #d9dcdf;
    --photo-office-deep: #8d949b;
    --photo-lounge: #6b4a3e;
    --photo-lounge-light: #d8d2c8;
    --photo-table: #c9c9c7;
    --photo-table-deep: #4a3a30;
  }
  * { margin: 0; padding: 0; box-sizing: border-box; }
  html, body {
    width: 1200px;
    height: 1200px;
    overflow: hidden;
    background: var(--paper);
  }
  .mailer {
    position: relative;
    width: 1200px;
    height: 1200px;
    background: var(--paper);
    overflow: hidden;
  }
  .photo-column {
    position: absolute;
    inset: 0;
    width: 1200px;
    height: 1200px;
  }
  .headline {
    position: absolute;
    left: 20px;
    top: 232px;
    width: 800px;
    text-align: center;
    font-family: "Montserrat", Arial, sans-serif;
    font-weight: 800;
    font-size: 128px;
    line-height: 142px;
    letter-spacing: -3px;
    color: var(--ink);
  }
  .headline .sale-word {
    display: block;
    text-transform: uppercase;
  }
  .tagline {
    position: absolute;
    left: 121px;
    top: 720px;
    width: 600px;
    text-align: center;
    font-family: "Montserrat", Arial, sans-serif;
    font-weight: 500;
    font-size: 29px;
    line-height: 41px;
    color: var(--ink);
  }
  .shop-button {
    position: absolute;
    left: 287px;
    top: 863px;
    width: 247px;
    height: 78px;
    background: var(--accent);
    color: var(--white);
    font-family: "Montserrat", Arial, sans-serif;
    font-weight: 700;
    font-size: 27px;
    line-height: 78px;
    text-align: center;
    letter-spacing: 0.5px;
  }
</style>
</head>
<body>
  <main class="mailer">
    <svg class="photo-column" viewBox="0 0 1200 1200" xmlns="http://www.w3.org/2000/svg">
      <defs>
        <linearGradient id="office-tone" x1="0" y1="0" x2="0" y2="1">
          <stop offset="0" stop-color="#eef0f2"/>
          <stop offset="0.6" stop-color="var(--photo-office)"/>
          <stop offset="1" stop-color="var(--photo-office-deep)"/>
        </linearGradient>
        <linearGradient id="lounge-tone" x1="0" y1="0" x2="0" y2="1">
          <stop offset="0" stop-color="var(--photo-lounge)"/>
          <stop offset="0.55" stop-color="#8a6d5e"/>
          <stop offset="0.75" stop-color="var(--photo-lounge-light)"/>
          <stop offset="1" stop-color="#6e625a"/>
        </linearGradient>
        <linearGradient id="table-tone" x1="0" y1="0" x2="0" y2="1">
          <stop offset="0" stop-color="#dcdcda"/>
          <stop offset="0.6" stop-color="var(--photo-table)"/>
          <stop offset="1" stop-color="var(--photo-table-deep)"/>
        </linearGradient>
      </defs>
      <polygon class="accent-wedge" points="907,480 1200,480 1200,1200 673,1200" fill="var(--accent)"/>
      <polygon class="photo photo-office" points="780,0 1200,0 1200,478 907,478" fill="url(#office-tone)" role="img" aria-label="Photo of a bright open office with a long white table, dark chairs and a sofa"/>
      <rect class="photo photo-lounge" x="868" y="483" width="332" height="436" fill="url(#lounge-tone)" role="img" aria-label="Photo of a white sofa with gold cushions against a brick wall with globe lamps"/>
      <rect class="photo photo-side-table" x="800" y="923" width="400" height="277" fill="url(#table-tone)" role="img" aria-label="Photo of a round wooden side table with a book and a vase of yellow flowers"/>
    </svg>

    <h1 class="headline">The big<br>furniture<span class="sale-word">sale</span></h1>
    <p class="tagline">Lorem ipsum dolor sit amet<br>Consectetur adipiscing elit</p>
    <div class="shop-button">SHOP NOW</div>
  </main>
</body>
</html>
```